Academy Values Classroom Poster

Marrowby Community Academy has the core values of Aspiration, Positivity, Responsibility and Achievement at its heart. We have these words displayed in our entrance (in Bliss font) but would like them to permeate into the classroom spaces in a poster form. We want a clear message that shows what the values mean to students:

Aspiration - Think BIG (pantone 717)
Positivity - Smile :-) (pantone 376)
Responsibility - for yourself and others (pantone 569)
Achievement - Celebrate Success! (pantone 214)

It would be good to follow the colour scheme of the main words to create a 'brand' for these values (pantone refs noted in brackets) and we would like to see some clean designs please.

I anticipate these will be A1 posters.

I have attached our school logo although it is not essential that this is included.

Target Market(s)

Students

Industry/Entity Type

School

Font styles to use
Other font styles liked:
• Bliss or Segoe UI

Requirements
Must have
• Aspiration - Think BIG
Positivity - Smile :-)
Responsibility - for yourself and others
Achievement - Celebrate Success!
Should not have
• Nothing too busy

```html
<!DOCTYPE html>
<html lang="en">
<head>
<meta charset="utf-8">
<title>Marrowby Community Academy – Our Values</title>
<link rel="stylesheet" href="https://fonts.googleapis.com/css2?family=Source+Sans+3:wght@400;600;700&display=swap">
<style>
  :root {
    --aspiration: #e8750f;
    --positivity: #84bd00;
    --responsibility: #00816d;
    --achievement: #ce0f69;
    --ring-white: #ffffff;
    --ink-navy: #1d3557;
    --bg-light: #e6edf1;
    --bg-mid: #9fb7c6;
    --bg-dark: #3b6580;
  }
  html, body {
    margin: 0;
    padding: 0;
    overflow: hidden;
  }
  .poster {
    position: relative;
    width: 849px;
    height: 1200px;
    overflow: hidden;
    background: radial-gradient(ellipse at 85% 5%, var(--bg-light) 0%, var(--bg-mid) 50%, var(--bg-dark) 100%);
    font-family: "Source Sans 3", "Segoe UI", sans-serif;
  }
  .academy-mark {
    position: absolute;
    top: 96px;
    left: 640px;
    display: flex;
    align-items: center;
    gap: 10px;
    width: 190px;
  }
  .academy-mark__square {
    flex: 0 0 34px;
    height: 34px;
    background: var(--ink-navy);
  }
  .academy-mark__name {
    font-weight: 600;
    font-size: 16px;
    line-height: 1.1;
    color: var(--ink-navy);
  }
  .values {
    position: absolute;
    inset: 0;
  }
  .value-title {
    font-weight: 600;
    fill: var(--ring-white);
  }
  .value-meaning {
    font-weight: 400;
  }
  .value--aspiration .value-meaning { fill: var(--aspiration); }
  .value--positivity .value-meaning { fill: var(--positivity); }
  .value--responsibility .value-meaning { fill: var(--responsibility); }
  .value--achievement .value-meaning { fill: var(--achievement); }
</style>
</head>
<body>
<main class="poster">
  <div class="academy-mark">
    <div class="academy-mark__square"></div>
    <div class="academy-mark__name">Marrowby Community Academy</div>
  </div>

  <svg class="values" width="849" height="1200" viewBox="0 0 849 1200" xmlns="http://www.w3.org/2000/svg">
    <defs>
      <radialGradient id="photo-aspiration" cx="50%" cy="40%" r="60%">
        <stop offset="0" stop-color="#e9e9e9"/><stop offset="1" stop-color="#8a8a8a"/>
      </radialGradient>
      <radialGradient id="photo-positivity" cx="50%" cy="40%" r="60%">
        <stop offset="0" stop-color="#d4d4d4"/><stop offset="1" stop-color="#5e5e5e"/>
      </radialGradient>
      <radialGradient id="photo-responsibility" cx="50%" cy="40%" r="60%">
        <stop offset="0" stop-color="#dcdcdc"/><stop offset="1" stop-color="#6f6f6f"/>
      </radialGradient>
      <radialGradient id="photo-achievement" cx="50%" cy="40%" r="60%">
        <stop offset="0" stop-color="#cfcfcf"/><stop offset="1" stop-color="#5a5a5a"/>
      </radialGradient>

      <path id="arc-aspiration-title" d="M325,510 A235,235 0 1 1 325,40 A235,235 0 1 1 325,510"/>
      <path id="arc-aspiration-meaning" d="M325,462 A187,187 0 1 1 325,88 A187,187 0 1 1 325,462"/>
      <path id="arc-positivity-title" d="M660,662 A177,177 0 1 1 660,308 A177,177 0 1 1 660,662"/>
      <path id="arc-positivity-meaning" d="M660,626 A141,141 0 1 1 660,344 A141,141 0 1 1 660,626"/>
      <path id="arc-responsibility-title" d="M330,1036 A241,241 0 1 1 330,554 A241,241 0 1 1 330,1036"/>
      <path id="arc-responsibility-meaning" d="M330,990 A195,195 0 1 1 330,600 A195,195 0 1 1 330,990"/>
      <path id="arc-achievement-title" d="M595,1207 A182,182 0 1 1 595,843 A182,182 0 1 1 595,1207"/>
      <path id="arc-achievement-meaning" d="M595,1171 A146,146 0 1 1 595,879 A146,146 0 1 1 595,1171"/>
    </defs>

    <g class="value value--aspiration">
      <circle cx="325" cy="275" r="268" fill="var(--ring-white)"/>
      <circle cx="325" cy="275" r="265" fill="var(--aspiration)"/>
      <circle cx="325" cy="275" r="205" fill="var(--ring-white)"/>
      <circle cx="325" cy="275" r="170" fill="url(#photo-aspiration)" role="img" aria-label="Photo of a smiling student in school uniform holding books"/>
      <text class="value-title" font-size="40" dominant-baseline="central">
        <textPath href="#arc-aspiration-title" startOffset="37%" text-anchor="middle">Aspiration - Think BIG</textPath>
      </text>
      <text class="value-meaning" font-size="21" dominant-baseline="central">
        <textPath href="#arc-aspiration-meaning" startOffset="24%" text-anchor="middle">a hope or ambition of achieving something</textPath>
      </text>
    </g>

    <g class="value value--positivity">
      <circle cx="660" cy="485" r="203" fill="var(--ring-white)"/>
      <circle cx="660" cy="485" r="200" fill="var(--positivity)"/>
      <circle cx="660" cy="485" r="155" fill="var(--ring-white)"/>
      <circle cx="660" cy="485" r="128" fill="url(#photo-positivity)" role="img" aria-label="Photo of happy children reading a book together"/>
      <text class="value-title" font-size="36" dominant-baseline="central">
        <textPath href="#arc-positivity-title" startOffset="55%" text-anchor="middle">Positivity - Smile :-)</textPath>
      </text>
      <text class="value-meaning" font-size="18" dominant-baseline="central">
        <textPath href="#arc-positivity-meaning" startOffset="66%" text-anchor="middle">a good, affirmative, or constructive quality or attitude</textPath>
      </text>
    </g>

    <g class="value value--responsibility">
      <circle cx="330" cy="795" r="273" fill="var(--ring-white)"/>
      <circle cx="330" cy="795" r="270" fill="var(--responsibility)"/>
      <circle cx="330" cy="795" r="212" fill="var(--ring-white)"/>
      <circle cx="330" cy="795" r="178" fill="url(#photo-responsibility)" role="img" aria-label="Photo of students walking to school with backpacks"/>
      <text class="value-title" font-size="38" dominant-baseline="central">
        <textPath href="#arc-responsibility-title" startOffset="30%" text-anchor="middle">Responsibility - for yourself and others</textPath>
      </text>
      <text class="value-meaning" font-size="21" dominant-baseline="central">
        <textPath href="#arc-responsibility-meaning" startOffset="5%" text-anchor="start">the opportunity to act independently and make decisions</textPath>
      </text>
    </g>

    <g class="value value--achievement">
      <circle cx="595" cy="1025" r="208" fill="var(--ring-white)"/>
      <circle cx="595" cy="1025" r="205" fill="var(--achievement)"/>
      <circle cx="595" cy="1025" r="160" fill="var(--ring-white)"/>
      <circle cx="595" cy="1025" r="132" fill="url(#photo-achievement)" role="img" aria-label="Photo of a student running a race on a sports field"/>
      <text class="value-title" font-size="32" dominant-baseline="central">
        <textPath href="#arc-achievement-title" startOffset="59%" text-anchor="middle">Achievement - Celebrate Success!</textPath>
      </text>
      <text class="value-meaning" font-size="18" dominant-baseline="central">
        <textPath href="#arc-achievement-meaning" startOffset="66%" text-anchor="middle">a thing done successfully, typically by effort, courage, or skill</textPath>
      </text>
    </g>
  </svg>
</main>
</body>
</html>
```